Business card templates for our website plus designer opportunity

we require 100 business card designs to start with in the following categories (see below ) please note we require 1000`s of designs in all types of different fields this is just a tester to check the response , we are currently setting up a inkpressly / printory type website/ marketplace we are now looking for freelance designers to make us some default designs to launch the site.

http://www.qorvelto.com/

Brief about qorvelto

we our a manufacture of a large range of products covering many industries we our currently setting up a marketplace where people can buy sell create and find personalized products and custom merchandised very much like printory and mugstacker we are now at the stage of adding content to the site for its launch we our currently looking for some core design templates in fact we need a lot of designs and we are currently looking for high quality designers to join our freelance design team .

The business cards designs

Please note all the text and data on the card can be the same so set up a default template to save yourself time all we really want is the core design front and back please , use inkpressly printory mug stacker for reference or ideas please make sure they are not copied and we have full rights to the any copyright your design may contain , if we pick your designs you we will paid for them asked to make another 200 designs and you will be asked if you would like to join our freelance qorvelto core design team you can always say no its perfectly fine but we have a lot of work to be designed for a lot of different products so there is a good opportunity here to get in before the site goes live in the next few months

Also note the chosen designs must be in vector format as well as jpeg and pdf , any vector files must be created to outlines
once we buy the designs we will own full rights to the copyright of said design and we can change and use these designs in anyway we see fit

Industry: ( 20 number designs for each ) Test run to check response

Agriculture & Farming
Animals & Pet Care
Art & Entertainment
Automotive & Transportation
Beauty & Spa

```html
<!DOCTYPE html>
<html lang="en">
<head>
<meta charset="utf-8">
<title>Qorvelto – Agriculture &amp; Farming Business Card</title>
<link href="https://fonts.googleapis.com/css2?family=Cinzel:wght@400&family=Lato:wght@400;700&display=swap" rel="stylesheet">
<style>
  :root {
    --page-bg: #d9d9d9;
    --card-black: #1a1a1a;
    --card-charcoal: #2b2b2b;
    --frame-line: #e6e6e6;
    --text-white: #f2f2f2;
    --text-muted: #cfcfcf;
    --accent-blue: #8cc3e6;
    --sky-top: #7fb7e6;
    --sky-low: #c9e1f2;
    --field-green: #5fa52a;
    --field-deep: #3f7c1c;
    --band-dark: rgba(30, 40, 30, 0.55);
  }
  * { box-sizing: border-box; margin: 0; padding: 0; }
  html, body { width: 1200px; height: 900px; overflow: hidden; }
  body {
    background: var(--page-bg);
    font-family: "Lato", sans-serif;
    display: flex;
    flex-direction: column;
    align-items: center;
    justify-content: center;
    gap: 50px;
  }
  .card {
    position: relative;
    width: 600px;
    height: 343px;
    border-radius: 3px;
    overflow: hidden;
    box-shadow: 0 10px 24px rgba(0, 0, 0, 0.25);
  }

  /* Back */
  .card-back {
    background: linear-gradient(135deg, var(--card-black), var(--card-charcoal) 55%, var(--card-black));
  }
  .back-frame { position: absolute; inset: 0; }
  .back-company {
    position: absolute;
    top: 130px; left: 0; right: 0;
    text-align: center;
    font-family: "Cinzel", serif;
    font-size: 27px;
    letter-spacing: 1.5px;
    color: var(--text-white);
  }
  .back-web {
    position: absolute;
    bottom: 36px; left: 0; right: 0;
    text-align: center;
    font-family: "Cinzel", serif;
    font-size: 10px;
    letter-spacing: 1px;
    color: var(--text-muted);
  }

  /* Front */
  .card-front { background: var(--card-black); }
  .front-photo {
    position: absolute;
    left: 0; top: 0; bottom: 0;
    width: 400px;
    background: linear-gradient(180deg, var(--sky-top) 0%, var(--sky-low) 52%, var(--field-green) 62%, var(--field-deep) 100%);
  }
  .front-fade {
    position: absolute;
    inset: 0;
    background: linear-gradient(90deg, rgba(26,26,26,0) 0%, rgba(26,26,26,0) 38%, rgba(26,26,26,0.85) 58%, var(--card-black) 68%, var(--card-charcoal) 100%);
  }
  .brand {
    position: absolute;
    left: 400px; top: 50px;
  }
  .brand-name {
    font-size: 25px;
    font-weight: 700;
    letter-spacing: 1px;
    color: var(--accent-blue);
    line-height: 1;
  }
  .brand-field {
    font-size: 12px;
    color: var(--text-white);
    margin-top: 4px;
    padding-left: 40px;
  }
  .person {
    position: absolute;
    right: 80px; top: 160px;
    text-align: center;
  }
  .person-name {
    font-size: 18px;
    letter-spacing: 0.5px;
    color: var(--text-white);
  }
  .person-name .first { color: var(--accent-blue); }
  .person-title {
    font-size: 8px;
    letter-spacing: 1px;
    color: var(--text-muted);
  }
  .contact {
    position: absolute;
    display: flex;
    align-items: center;
    gap: 12px;
    font-size: 12px;
    line-height: 1.3;
    color: var(--text-white);
  }
  .contact svg { flex: none; }
  .contact-web { right: 70px; top: 232px; }
  .contact-phone { left: 315px; top: 270px; }
  .address-band {
    position: absolute;
    left: 0; bottom: 0;
    width: 370px; height: 52px;
    background: var(--band-dark);
  }
  .contact-address { left: 24px; bottom: 10px; color: var(--text-muted); }
</style>
</head>
<body>

<section class="card card-back" aria-label="Business card back">
  <svg class="back-frame" width="600" height="343" viewBox="0 0 600 343">
    <g fill="none" stroke="var(--frame-line)" stroke-width="1.5">
      <polyline points="195,305 50,305 50,38 550,38 550,300 430,300"/>
    </g>
  </svg>
  <h1 class="back-company">Company Name</h1>
  <p class="back-web">www.qorvelto.com</p>
</section>

<section class="card card-front" aria-label="Business card front">
  <div class="front-photo" role="img" aria-label="Photo of a green tractor working a green field under a clear blue sky"></div>
  <div class="front-fade"></div>

  <div class="brand">
    <h2 class="brand-name">QORVELTO</h2>
    <p class="brand-field">Agriculture &amp; Farming</p>
  </div>

  <div class="person">
    <p class="person-name"><span class="first">DANIEL</span> HARROW</p>
    <p class="person-title">PRESIDENT</p>
  </div>

  <div class="contact contact-web">
    <svg width="20" height="20" viewBox="0 0 20 20" fill="none" stroke="var(--text-white)" stroke-width="1.3">
      <circle cx="10" cy="10" r="8.5"/>
      <ellipse cx="10" cy="10" rx="3.8" ry="8.5"/>
      <line x1="1.5" y1="10" x2="18.5" y2="10"/>
      <line x1="3" y1="5.5" x2="17" y2="5.5"/>
      <line x1="3" y1="14.5" x2="17" y2="14.5"/>
    </svg>
    <p>contact@qorvelto.com<br>www.qorvelto.com</p>
  </div>

  <div class="contact contact-phone">
    <svg width="18" height="18" viewBox="0 0 24 24" fill="var(--text-white)">
      <path d="M6.6 10.8a15.1 15.1 0 0 0 6.6 6.6l2.2-2.2a1 1 0 0 1 1-.25 11.4 11.4 0 0 0 3.6.57 1 1 0 0 1 1 1V20a1 1 0 0 1-1 1A17 17 0 0 1 3 4a1 1 0 0 1 1-1h3.5a1 1 0 0 1 1 1c0 1.25.2 2.45.57 3.57a1 1 0 0 1-.25 1z"/>
    </svg>
    <p>555 014 2270<br>555 018 9364</p>
  </div>

  <div class="address-band"></div>
  <div class="contact contact-address">
    <svg width="20" height="18" viewBox="0 0 24 22" fill="var(--text-white)">
      <path d="M12 2 1 11h3v9h6v-6h4v6h6v-9h3z"/>
    </svg>
    <p>48 Meadow Ln.<br>Fairbrook, IL 60999</p>
  </div>
</section>

</body>
</html>
```